Business card for my company-RMK Design Studio

I do not have a logo-I like red and keeping it clean. Information that should be on the card:
Tom Brakefield AIA
Architecture Planning Interiors
Cell Phone-614.492.5068
email-rmkarchitect1@lunvale.com
www.rmkdesignstudio.net

```html
<!DOCTYPE html>
<html lang="en">
<head>
<meta charset="utf-8">
<title>RMK Design Studio – Business Card</title>
<link rel="stylesheet" href="https://fonts.googleapis.com/css2?family=Bodoni+Moda:opsz,wght@6..96,400;6..96,500;6..96,700&display=swap">
<style>
  :root {
    --backdrop: #d8d3cb;
    --card-light: #ffffff;
    --card-dark: #2a2a2a;
    --brand-red: #e3242b;
    --ink: #111111;
    --rule: #a9a9a9;
    --reverse: #ffffff;
  }
  * { margin: 0; padding: 0; box-sizing: border-box; }
  html, body {
    width: 900px;
    height: 1200px;
    overflow: hidden;
  }
  body {
    position: relative;
    background: var(--backdrop);
    font-family: "Bodoni Moda", "Didot", serif;
    color: var(--ink);
  }
  .card {
    position: absolute;
    left: 82px;
    width: 733px;
    height: 428px;
    border-radius: 28px;
    box-shadow: 0 6px 10px rgba(0, 0, 0, 0.35);
    overflow: hidden;
  }
  .card--front { top: 138px; background: var(--card-light); }
  .card--back  { top: 634px; background: var(--card-dark); }

  .studio-title {
    position: absolute;
    right: 38px;
    top: 44px;
    font-size: 46px;
    font-weight: 500;
    color: var(--brand-red);
    line-height: 1;
    letter-spacing: 0.5px;
  }
  .title-rule {
    position: absolute;
    left: 0;
    right: 0;
    top: 97px;
    height: 1px;
    background: var(--rule);
  }
  .holder-name {
    position: absolute;
    left: 41px;
    top: 110px;
    font-size: 28px;
    font-weight: 500;
    letter-spacing: 0.6px;
    line-height: 1;
  }
  .holder-disciplines {
    position: absolute;
    left: 41px;
    top: 148px;
    font-size: 14px;
    font-weight: 700;
    line-height: 1;
  }
  .contact {
    position: absolute;
    left: 41px;
    top: 323px;
    font-size: 17px;
    font-weight: 700;
    line-height: 27px;
    letter-spacing: 0.3px;
  }
  .website {
    position: absolute;
    right: 38px;
    top: 350px;
    font-size: 17px;
    font-weight: 700;
    line-height: 27px;
    letter-spacing: 0.3px;
  }
  .wordmark {
    position: absolute;
    left: 0;
    right: 0;
    top: 175px;
    text-align: center;
    font-size: 62px;
    font-weight: 500;
    line-height: 1;
    color: var(--reverse);
  }
</style>
</head>
<body>
  <section class="card card--front" aria-label="Business card front">
    <h1 class="studio-title">RMK Design Studio</h1>
    <div class="title-rule"></div>
    <p class="holder-name">Tom Brakefield AIA</p>
    <p class="holder-disciplines">Architecture Planning Interiors</p>
    <p class="contact">
      Cell : -614.492.5068<br>
      Email : rmkarchitect1@lunvale.com
    </p>
    <p class="website">www.rmkdesignstudio.net</p>
  </section>

  <section class="card card--back" aria-label="Business card back">
    <p class="wordmark">RMK Design Studio</p>
  </section>
</body>
</html>
```